Live Band Music Series on Beach Flyer

Driftwood Cove Resort at Monterey Bay, California is introducing a Music Series "Tunes by the Tide", offering every Sunday starting April 16, 2023 from 2:30pm - 4:00PM. These are live bands performing for free on our beach. We would need the dates and times as well as our logo in a fun, family-oriented and beach/ wave/ cliff themed flyer. The phrase 'Surf’s Up!' can be included as well.
Event dates are April 16, April 23, April 30 and May 7 and information are available at our Event Calendar at driftwoodcoveresort.com
NOTE TO DESIGNER: Based on success we may extend throughout summer

```html
<!DOCTYPE html>
<html lang="en">
<head>
<meta charset="utf-8">
<title>Tunes by the Tide — Driftwood Cove Resort</title>
<link rel="stylesheet" href="https://fonts.googleapis.com/css2?family=Libre+Caslon+Text:wght@400&family=Montserrat:wght@300;500&display=swap">
<style>
  :root {
    --navy: #1a3c69;
    --navy-deep: #13304f;
    --gold: #b39a6b;
    --gold-line: #9d875c;
    --white: #ffffff;
    --soft-white: #e4e8ef;
  }
  * { margin: 0; padding: 0; box-sizing: border-box; }
  html, body {
    width: 848px;
    height: 1200px;
    overflow: hidden;
    background: var(--navy);
  }
  .flyer {
    position: relative;
    width: 848px;
    height: 1200px;
    background: var(--navy);
    font-family: "Montserrat", sans-serif;
    color: var(--white);
  }
  .frame {
    position: absolute;
    left: 36px;
    top: 35px;
    width: 773px;
    height: 1120px;
    border: 1.5px solid var(--gold-line);
  }
  .brand {
    position: absolute;
    top: 104px;
    left: 0;
    width: 100%;
    text-align: center;
    font-family: "Libre Caslon Text", serif;
    font-size: 26px;
    color: var(--white);
    letter-spacing: 0.5px;
  }
  .title {
    position: absolute;
    left: 0;
    width: 100%;
    text-align: center;
    font-family: "Libre Caslon Text", serif;
    font-weight: 400;
    color: var(--gold);
    line-height: 1;
  }
  .title-main { top: 190px; font-size: 104px; letter-spacing: 2px; }
  .title-sub { top: 304px; font-size: 48px; letter-spacing: 1px; }
  .photo {
    position: absolute;
    left: 104px;
    top: 382px;
    width: 637px;
    height: 469px;
    background:
      radial-gradient(circle at 38% 22%, #fff6dc 0%, #ffd98a 14%, rgba(240,160,70,0.6) 34%, rgba(0,0,0,0) 60%),
      linear-gradient(180deg, #f3b25a 0%, #c9782f 45%, #6e3c1c 100%);
  }
  .schedule {
    position: absolute;
    left: 36px;
    top: 890px;
    width: 773px;
    height: 103px;
    display: flex;
    border-top: 1.5px solid var(--gold-line);
    border-bottom: 1.5px solid var(--gold-line);
  }
  .date {
    flex: 1;
    display: flex;
    align-items: center;
    justify-content: center;
    font-weight: 300;
    font-size: 28px;
    color: var(--soft-white);
    border-right: 1.5px solid var(--gold-line);
  }
  .date:last-child { border-right: none; }
  .time {
    position: absolute;
    top: 1030px;
    left: 0;
    width: 100%;
    text-align: center;
    font-weight: 300;
    font-size: 28px;
    color: var(--soft-white);
  }
  .info {
    position: absolute;
    left: 37px;
    top: 1096px;
    width: 771px;
    height: 58px;
    background: var(--navy-deep);
    display: flex;
    align-items: center;
    justify-content: center;
    font-weight: 300;
    font-size: 18px;
    color: var(--soft-white);
  }
  .info .url { font-weight: 500; color: var(--white); margin-left: 6px; }
</style>
</head>
<body>
  <main class="flyer">
    <div class="frame"></div>
    <div class="brand">Driftwood Cove Resort</div>
    <h1 class="title title-main">TUNES</h1>
    <h2 class="title title-sub">BY THE TIDE</h2>
    <div class="photo" role="img" aria-label="Photo of young people dancing on the beach at sunset, backlit by golden sun"></div>
    <div class="schedule">
      <div class="date">APRIL 16</div>
      <div class="date">APRIL 23</div>
      <div class="date">APRIL 30</div>
      <div class="date">MAY&nbsp;&nbsp;07</div>
    </div>
    <p class="time">2:30PM - 4:00PM.</p>
    <p class="info">Information are available at our Event Calendar at <span class="url">driftwoodcoveresort.com</span></p>
  </main>
</body>
</html>
```